I need a flyer made , the flyer can be one page or two pages or three pages . I will be posting this on Instagram and social media platforms. I am a luxury home builder , I am looking to hire a construction project manager . Below are some examples and ideas what can be on the flyer

We’re looking for a construction project manager who’s passionate about building luxury homes at the highest standards
We’re hiring construction project manager
* Experience 5+ years in residential project management with a strong portfolio of completed homes.
* location : Bergen County NJ
* excellent leadership skills, leads teams with confidence and clarity
* communicates seamlessly with architects , engineers, designers and clients
*knows how to manage budgets and timelines without compromising quality
*solves problems with a positive solution first mindset
* pays attention to every detail because in luxury the small things are the big things

Apply now , link in bio or DM to connect.

My logo is attached, my web site www.ridgelanebuilders.com
My style is modern but still warm and inviting. I like a clean classy look .
Updates

Please don’t add any images of chairs or people to the flyer , I do not want people on my flyer. Do not add standard images of offices and houses , we are luxury builders , we build homes over 2 million dollars. Keep a classy , simple modern look . High end .

You can add a white hard hat with my logo on it for a image , this is a suggestion does not have to be on my flyer ,

```html
<!DOCTYPE html>
<html lang="en">
<head>
<meta charset="UTF-8">
<title>Ridgelane Builders – Construction Project Manager</title>
<link href="https://fonts.googleapis.com/css2?family=Cinzel:wght@500&family=Montserrat:wght@600;700&family=Poppins:wght@400;600&family=Yesteryear&display=swap" rel="stylesheet">
<style>
  :root{
    --ink:#000000;
    --paper:#ffffff;
    --stone:#dedddb;
    --text:#111111;
    --rule:#b9b9b9;
    --photo-dark:#2f4257;
    --photo-light:#8fa3b3;
  }
  html,body{margin:0;padding:0;overflow:hidden;background:var(--paper);}
  .flyer{position:relative;width:1200px;height:1200px;overflow:hidden;background:var(--paper);font-family:"Poppins",sans-serif;color:var(--text);}
  .header-band{position:absolute;left:0;top:0;width:1200px;height:191px;background:var(--ink);}
  .brand-name{position:absolute;left:56px;top:52px;width:520px;margin:0;font-family:"Cinzel",serif;font-weight:500;font-size:46px;line-height:58px;letter-spacing:2px;color:var(--paper);text-transform:uppercase;}
  .job-title{position:absolute;right:24px;top:30px;margin:0;text-align:right;font-family:"Cinzel",serif;font-weight:500;font-size:50px;line-height:58px;letter-spacing:2px;color:var(--paper);}
  .accent-bar-top{position:absolute;left:853px;top:169px;width:347px;height:55px;background:var(--stone);}
  .join-script{position:absolute;right:22px;top:244px;margin:0;font-family:"Yesteryear",cursive;font-size:60px;letter-spacing:5px;color:var(--ink);}
  .headline{position:absolute;left:40px;top:258px;margin:0;font-family:"Montserrat",sans-serif;color:var(--ink);}
  .headline .small{display:block;font-weight:700;font-size:64px;line-height:64px;letter-spacing:1px;}
  .headline .big{display:block;font-weight:600;font-size:116px;line-height:120px;letter-spacing:1px;margin-top:2px;}
  .dashed-rule{position:absolute;left:0;top:444px;width:590px;border-top:2px dashed var(--rule);}
  .requirements{position:absolute;left:40px;top:476px;width:560px;margin:0;padding:0;list-style:none;font-size:18px;line-height:28px;}
  .requirements li{position:relative;padding-left:37px;margin-bottom:9px;}
  .requirements li.single{margin-bottom:9px;}
  .requirements .tick{position:absolute;left:2px;top:7px;width:15px;height:15px;}
  .apply-button{position:absolute;left:62px;top:897px;width:230px;height:76px;background:var(--ink);color:var(--paper);display:flex;align-items:center;justify-content:center;font-family:"Cinzel",serif;font-weight:500;font-size:29px;letter-spacing:1px;}
  .accent-square{position:absolute;left:0;top:973px;width:61px;height:36px;background:var(--stone);}
  .footer-band{position:absolute;left:0;top:998px;width:1200px;height:202px;background:var(--ink);}
  .photo-backing{position:absolute;left:661px;top:347px;width:479px;height:97px;background:var(--stone);}
  .photo-frame{position:absolute;left:681px;top:367px;width:519px;height:689px;background:var(--paper);}
  .photo{position:absolute;left:694px;top:378px;width:506px;height:670px;background:linear-gradient(160deg,var(--photo-dark) 0%,#4d6378 45%,var(--photo-light) 100%);}
  .connect-line{position:absolute;left:41px;top:1068px;margin:0;font-weight:600;font-size:17px;color:var(--paper);}
  .website{position:absolute;left:44px;top:1108px;margin:0;font-family:"Cinzel",serif;font-weight:500;font-size:22px;letter-spacing:2px;color:var(--paper);text-transform:uppercase;}
  .accent-bar-bottom{position:absolute;left:756px;top:1167px;width:444px;height:33px;background:var(--stone);}
</style>
</head>
<body>
<main class="flyer">
  <div class="header-band"></div>
  <p class="brand-name">Ridgelane Builders</p>
  <h1 class="job-title">Construction<br>Project Manager</h1>
  <div class="accent-bar-top"></div>

  <p class="join-script">Join Our Team</p>

  <h2 class="headline"><span class="small">WE ARE</span><span class="big">HIRING!</span></h2>
  <div class="dashed-rule"></div>

  <ul class="requirements">
    <li><svg class="tick" viewBox="0 0 16 16"><circle cx="8" cy="8" r="6.5" fill="none" stroke="#111" stroke-width="1.4"/><path d="M4.8 8.2l2.3 2.2L14 3.4" fill="none" stroke="#111" stroke-width="1.6"/></svg>Experience 5+ Years In Residential Project Management With A Strong Portfolio Of Completed Homes.</li>
    <li class="single"><svg class="tick" viewBox="0 0 16 16"><circle cx="8" cy="8" r="6.5" fill="none" stroke="#111" stroke-width="1.4"/><path d="M4.8 8.2l2.3 2.2L14 3.4" fill="none" stroke="#111" stroke-width="1.6"/></svg>Location : Bergen County NJ</li>
    <li><svg class="tick" viewBox="0 0 16 16"><circle cx="8" cy="8" r="6.5" fill="none" stroke="#111" stroke-width="1.4"/><path d="M4.8 8.2l2.3 2.2L14 3.4" fill="none" stroke="#111" stroke-width="1.6"/></svg>Excellent Leadership Skills, Leads Teams With Confidence And Clarity</li>
    <li><svg class="tick" viewBox="0 0 16 16"><circle cx="8" cy="8" r="6.5" fill="none" stroke="#111" stroke-width="1.4"/><path d="M4.8 8.2l2.3 2.2L14 3.4" fill="none" stroke="#111" stroke-width="1.6"/></svg>Communicates Seamlessly With Architects , Engineers, Designers And Clients</li>
    <li><svg class="tick" viewBox="0 0 16 16"><circle cx="8" cy="8" r="6.5" fill="none" stroke="#111" stroke-width="1.4"/><path d="M4.8 8.2l2.3 2.2L14 3.4" fill="none" stroke="#111" stroke-width="1.6"/></svg>Knows How To Manage Budgets And Timelines Without Compromising Quality</li>
    <li class="single"><svg class="tick" viewBox="0 0 16 16"><circle cx="8" cy="8" r="6.5" fill="none" stroke="#111" stroke-width="1.4"/><path d="M4.8 8.2l2.3 2.2L14 3.4" fill="none" stroke="#111" stroke-width="1.6"/></svg>Solves Problems With A Positive Solution First Mindset</li>
    <li><svg class="tick" viewBox="0 0 16 16"><circle cx="8" cy="8" r="6.5" fill="none" stroke="#111" stroke-width="1.4"/><path d="M4.8 8.2l2.3 2.2L14 3.4" fill="none" stroke="#111" stroke-width="1.6"/></svg>Pays Attention To Every Detail Because In Luxury The Small Things Are The Big Things</li>
  </ul>

  <div class="footer-band"></div>
  <div class="apply-button">Apply now</div>
  <div class="accent-square"></div>

  <div class="photo-backing"></div>
  <div class="photo-frame"></div>
  <div class="photo" role="img" aria-label="Photograph of a construction project manager in a white hard hat and high-visibility vest, standing with arms crossed in front of a building"></div>

  <p class="connect-line">Link In Bio Or DM To Connect.</p>
  <p class="website">www.ridgelanebuilders.com</p>
  <div class="accent-bar-bottom"></div>
</main>
</body>
</html>
```